NORDIC HERON WEBSITE DESIGN

We need a website designed for Nordic Heron Timepieces, its a watch brand which originated from switzerland, you will get data on nordic heron on www.nordicherontime.example.

The website needs to be a combination of the following websites.

http://www.kolvarine.example/int-en/home
http://www.dunstable-ferro.example/en/

The look of the website should be very luxury and classy, should look like a swiss website with a lot of swiss imagery of mountains, etc.

The website will be an online shopping website, so should have add to card, shopping link etc...

Target Market(s)

Successful people who have arrived in LIFE

Age : 30-45 managerial class people

Industry/Entity Type

Online Shopping

Font styles to use
Sans Serif

Colors

Designer to choose colors to be used in the design.

Requirements
Must have
• Flash banners on the homepage
Swiss feel on the website is a must

```html
<!DOCTYPE html>
<html lang="en">
<head>
<meta charset="utf-8">
<title>Nordic Heron Timepieces – Support</title>
<link rel="stylesheet" href="https://fonts.googleapis.com/css2?family=Questrial&family=Raleway:wght@200;300&display=swap">
<style>
  :root {
    --brand-red: #e31a3c;
    --band-red: #c9203b;
    --black: #000000;
    --panel: rgba(18, 18, 18, 0.88);
    --field: #c9c9c9;
    --text-light: #ffffff;
    --text-soft: #e6e6e6;
    --footer-bg: #1f1f1f;
    --rule: #9a9a9a;
  }
  * { box-sizing: border-box; margin: 0; padding: 0; }
  html, body { width: 1200px; height: 1095px; overflow: hidden; background: var(--black); }
  body { font-family: "Questrial", sans-serif; color: var(--text-light); }
  .page { position: relative; width: 1200px; height: 1095px; overflow: hidden; }

  /* Top utility bar */
  .utility-bar { position: absolute; left: 0; top: 0; width: 1200px; height: 29px; background: var(--brand-red); }
  .utility-link { position: absolute; top: 9px; font-size: 10px; display: flex; align-items: center; gap: 6px; color: var(--text-light); text-decoration: none; }
  .utility-link.account { left: 900px; }
  .utility-link.cart { left: 1000px; }

  /* Main navigation */
  .main-nav { position: absolute; left: 0; top: 29px; width: 1200px; height: 65px; background: var(--black); }
  .main-nav ul { list-style: none; position: absolute; right: 113px; top: 17px; display: flex; gap: 43px; }
  .main-nav a { color: var(--text-light); text-decoration: none; font-size: 15px; letter-spacing: 0.2px; }

  /* Brand pennant */
  .brand-pennant { position: absolute; left: 98px; top: 0; width: 148px; height: 147px; z-index: 3; }
  .brand-pennant svg { position: absolute; inset: 0; }
  .brand-name { position: absolute; left: 0; right: 0; top: 56px; text-align: center; font-size: 15px; line-height: 1.3; color: var(--text-light); letter-spacing: 1px; }
  .brand-mark { position: absolute; left: 62px; top: 24px; width: 24px; height: 24px; background: var(--brand-red); }

  /* Hero backdrop */
  .hero-backdrop { position: absolute; left: 0; top: 94px; width: 1200px; height: 772px;
    background:
      radial-gradient(ellipse 520px 420px at 830px 360px, #9a9a9a 0%, #5e5e5e 45%, rgba(20,20,20,0) 80%),
      radial-gradient(ellipse 380px 300px at 1120px 120px, #d4d4d4 0%, rgba(80,80,80,0) 70%),
      linear-gradient(90deg, #030303 0%, #1a1a1a 30%, #3a3a3a 70%, #2b2b2b 100%); }

  /* Support panel */
  .support-panel { position: absolute; left: 98px; top: 201px; width: 737px; height: 468px; background: var(--panel); }
  .panel-title { position: absolute; left: 36px; top: 20px; display: flex; align-items: center; gap: 10px;
    font-family: "Raleway", sans-serif; font-weight: 200; font-size: 42px; letter-spacing: 3px; }
  .title-mark { width: 30px; height: 30px; border-radius: 50%; background: var(--brand-red); }
  .collapse-bar { position: absolute; left: 676px; top: 31px; width: 38px; height: 8px; background: var(--brand-red); }
  .panel-intro { position: absolute; left: 36px; top: 103px; font-size: 15px; letter-spacing: 0.8px; color: var(--text-soft); }

  .field-label { position: absolute; font-size: 15px; letter-spacing: 1px; color: var(--text-soft); text-align: right; }
  .field { position: absolute; height: 29px; background: var(--field); border: 0; font-family: "Questrial", sans-serif; font-size: 13px; padding: 0 10px; color: #222; }
  .field::placeholder { color: #222; }
  .field.message { height: 79px; resize: none; padding-top: 8px; }
  .send-button { position: absolute; left: 168px; top: 364px; width: 188px; height: 38px; background: var(--brand-red); border: 0; color: var(--text-light);
    font-family: "Questrial", sans-serif; font-size: 15px; letter-spacing: 1px; }

  /* Registration band */
  .registration-band { position: absolute; left: 100px; top: 687px; width: 738px; height: 81px; background: var(--band-red); }
  .registration-band .panel-title { top: 18px; left: 36px; }
  .registration-band .title-mark { background: var(--text-light); }
  .expand-icon { position: absolute; left: 697px; top: 29px; }

  /* Footer */
  .site-footer { position: absolute; left: 0; top: 866px; width: 1200px; height: 186px;
    background: linear-gradient(180deg, #2a2a2a 0%, #1c1c1c 55%, #121212 100%); }
  .footer-heading { position: absolute; top: 34px; font-size: 17px; padding-bottom: 6px; border-bottom: 1px solid var(--rule); color: var(--text-light); }
  .footer-links { position: absolute; left: 123px; top: 88px; display: grid; grid-template-columns: 122px 120px; row-gap: 14px; list-style: none; }
  .footer-links a { color: var(--text-light); text-decoration: none; font-size: 13px; }
  .social-list { position: absolute; left: 502px; top: 78px; display: flex; gap: 8px; list-style: none; }
  .social-list li { width: 34px; height: 34px; border-radius: 50%; background: #d8d8d8; }
  .newsletter { position: absolute; left: 856px; top: 74px; display: flex; }
  .newsletter-input { width: 170px; height: 31px; border: 0; background: #ffffff; padding: 0 9px; font-family: "Questrial", sans-serif; font-size: 13px; font-style: normal; }
  .newsletter-input::placeholder { color: #9a9a9a; }
  .newsletter-submit { width: 77px; height: 31px; border: 0; background: var(--black); color: var(--text-light); font-family: "Questrial", sans-serif; font-size: 13px; }

  /* Legal bar */
  .legal-bar { position: absolute; left: 0; top: 1052px; width: 1200px; height: 43px; background: var(--black); font-size: 10px; }
  .copyright { position: absolute; left: 123px; top: 16px; }
  .legal-links { position: absolute; right: 153px; top: 19px; display: flex; gap: 8px; list-style: none; }
  .legal-links a { color: var(--text-light); text-decoration: none; }
</style>
</head>
<body>
<div class="page">
  <header>
    <div class="utility-bar">
      <a class="utility-link account" href="#">
        <svg width="11" height="11" viewBox="0 0 11 11" aria-hidden="true"><circle cx="5.5" cy="3" r="2.6" fill="#fff"/><path d="M0.5 11 C0.5 7 10.5 7 10.5 11 Z" fill="#fff"/></svg>
        My Account</a>
      <a class="utility-link cart" href="#">
        <svg width="13" height="11" viewBox="0 0 13 11" aria-hidden="true"><path d="M0.5 1 H3 L4.5 7 H11 L12.5 2.5 H3.6" fill="none" stroke="#fff" stroke-width="1.3"/><circle cx="5.5" cy="9.5" r="1.1" fill="#fff"/><circle cx="10" cy="9.5" r="1.1" fill="#fff"/></svg>
        Shopping Cart</a>
    </div>
    <nav class="main-nav">
      <ul>
        <li><a href="#">HOME</a></li>
        <li><a href="#">NORDIC HERON</a></li>
        <li><a href="#">COLLECTION</a></li>
        <li><a href="#">PRESS</a></li>
        <li><a href="#">SUPPORT</a></li>
        <li><a href="#">CONTACT</a></li>
      </ul>
    </nav>
    <div class="brand-pennant">
      <svg width="148" height="147" viewBox="0 0 148 147" aria-hidden="true"><path d="M0 0 H148 V125 L74 147 L0 125 Z" fill="#000" stroke="#2a2a2a" stroke-width="1"/></svg>
      <span class="brand-mark"></span>
      <div class="brand-name">NORDIC<br>HERON</div>
    </div>
  </header>

  <main>
    <div class="hero-backdrop" role="img" aria-label="Monochrome close-up photograph of a watchmaker's tools working on an open watch movement"></div>

    <section class="support-panel">
      <h1 class="panel-title"><span class="title-mark"></span>SUPPORT</h1>
      <span class="collapse-bar"></span>
      <p class="panel-intro">Customers can contact us by E-mail at anytime.</p>

      <label class="field-label" style="left:40px; top:155px; width:122px;">Firstname:</label>
      <input class="field" style="left:168px; top:144px; width:188px;" type="text">
      <label class="field-label" style="left:360px; top:155px; width:120px;">Lastname:</label>
      <input class="field" style="left:482px; top:144px; width:188px;" type="text">

      <label class="field-label" style="left:40px; top:214px; width:122px;">Phone:</label>
      <input class="field" style="left:168px; top:204px; width:188px;" type="text" placeholder="xxx-xxxx-xxxx-xx">
      <label class="field-label" style="left:360px; top:209px; width:120px;">Email:</label>
      <input class="field" style="left:483px; top:200px; width:188px;" type="email">

      <label class="field-label" style="left:40px; top:270px; width:120px;">Message:</label>
      <textarea class="field message" style="left:168px; top:259px; width:502px;"></textarea>

      <button class="send-button" type="button">Send Message</button>
    </section>

    <section class="registration-band">
      <h2 class="panel-title"><span class="title-mark"></span>REGISTRTION</h2>
      <svg class="expand-icon" width="24" height="24" viewBox="0 0 24 24" aria-hidden="true"><rect x="8.5" y="0" width="7" height="24" fill="#fff"/><rect x="0" y="8.5" width="24" height="7" fill="#fff"/></svg>
    </section>
  </main>

  <footer>
    <div class="site-footer" role="img" aria-label="Dark photograph of a rocky coastline">
      <h3 class="footer-heading" style="left:121px; width:257px;">NAVIGATION</h3>
      <ul class="footer-links">
        <li><a href="#">HOME</a></li><li><a href="#">PRESS</a></li>
        <li><a href="#">NORDIC HERON</a></li><li><a href="#">SUPPORT</a></li>
        <li><a href="#">COLLECTION</a></li><li><a href="#">CONTACT</a></li>
      </ul>

      <h3 class="footer-heading" style="left:502px; width:175px;">KEEP IN TOUCH</h3>
      <ul class="social-list" aria-label="Social channels">
        <li></li><li></li><li></li><li></li>
      </ul>

      <h3 class="footer-heading" style="left:854px; width:259px;">JOIN TO OUR NEWSLETTER</h3>
      <form class="newsletter">
        <input class="newsletter-input" type="email" placeholder="EMAIL ADDRESS">
        <button class="newsletter-submit" type="button">SUBMIT</button>
      </form>
    </div>
    <div class="legal-bar">
      <p class="copyright">COPYRIGHT © NORDIC HERON 2014</p>
      <ul class="legal-links">
        <li><a href="#">SITEMAP</a></li><li>-</li>
        <li><a href="#">FAQ</a></li><li>-</li>
        <li><a href="#">PRIVACY POLICY</a></li>
      </ul>
    </div>
  </footer>
</div>
</body>
</html>
```